The 318 Principle (An Album CD Cover)

Design a CD cover, front and back, based on the images that I've uploaded.
Front - I'd like the picture with the white t-shirt in which I'm staring into the camera to be the front cover. I'd like the picture to have an oil painting effect with half of the body disintegrating like a sand storm effect (i've attached a sample image). I want the entire front cover to be bordered in a classic looking gold frame (think Vela Corin frame and a renaissance feeling). Within the frame, at the top, it should read: R.O.V.E.N.T.A Marsh (centered). Within the frame, at the bottom, it should read: The 318 Principle: Echoes of Breathing (centered w/ Side Effects... on the second line). This font should maybe be some sort of brush strokes to work with the bordered artwork.
Back - The back should utilize the picture with the black t-shirt. This should also resemble an oil painting, but without a frame or the sand storm effect. Over top of this picture the following track list should be included:
1. Hollow Rooms
2. Calm Ruler
3. Fresh Mess
4. Block Visions
5. Brotha Workshop
6. Anyone to Hold
7. August Evenings
8. Mae
9. Faith is my Anchor
10. Tangles
11. Proclaim
12. Jubilee
13. Our Thread
14. Queen Chief
15. 318
16. Picture

Please don't hesitate to contact me for clarity on the project.

Thanks,
Dwayne

Target Market(s)

28-40 year olds

Requirements
Must have
• Cover must draw people in and force them to want to listen to hear the album. It must have a classic, timeless feel. I don't want the image to ever look old, so it shouldn't look contemporary.
Nice to have
• The album is about how a particular day shaped my life. So, the font of the album title should be humanistic and artistic, but the font of the name of the artist, R.O.V.E.N.T.A Marsh, can be in a font that fits, but not necessarily the same font as the album title.
Should not have
• While I've requested some graphic effects, the art must not look cheesy.

```html
<!DOCTYPE html>
<html lang="en">
<head>
<meta charset="utf-8">
<title>The 318 Principle — CD Cover</title>
<link href="https://fonts.googleapis.com/css2?family=Alfa+Slab+One&family=Crimson+Text:wght@400;600&display=swap" rel="stylesheet">
<style>
  :root {
    --backdrop: #6e4128;
    --sage-light: #d3d8c2;
    --sage-mid: #b3bca2;
    --sage-dark: #96a186;
    --slate-light: #a6b09f;
    --slate-dark: #6f7d6c;
    --ink-white: #ffffff;
    --ink-shadow: rgba(30, 30, 25, 0.7);
    --divider: #ffffff;
    --gold-pale: #f7e39a;
    --gold-light: #e2b954;
    --gold-mid: #b7852a;
    --gold-dark: #6e4a10;
    --gold-deep: #4a300a;
  }
  html, body {
    margin: 0;
    padding: 0;
    width: 1200px;
    height: 1000px;
    overflow: hidden;
    background: var(--backdrop);
  }
  .canvas {
    position: relative;
    width: 1200px;
    height: 1000px;
  }
  .panel {
    position: absolute;
    top: 228px;
    width: 549px;
    height: 544px;
    overflow: hidden;
    box-shadow: 0 0 0 1px rgba(255,255,255,0.6), 0 3px 10px rgba(0,0,0,0.45);
  }
  /* Back cover */
  .back-cover {
    left: 42px;
    background: radial-gradient(ellipse at 50% 55%, var(--sage-light) 0%, var(--sage-mid) 55%, var(--sage-dark) 100%);
  }
  .tracklist {
    position: absolute;
    top: 32px;
    margin: 0;
    padding: 0;
    list-style: none;
    white-space: nowrap;
    font-family: "Alfa Slab One", Georgia, serif;
    font-size: 13px;
    line-height: 18.3px;
    letter-spacing: 1.2px;
    color: var(--ink-white);
    text-shadow: 0 0 2px var(--ink-shadow), 1px 1px 1px var(--ink-shadow);
  }
  .tracklist-side-a {
    right: 286px;
    text-align: right;
  }
  .tracklist-side-b {
    left: 286px;
    text-align: left;
  }
  .tracklist-divider {
    position: absolute;
    left: 274px;
    top: 28px;
    width: 1.5px;
    height: 158px;
    background: var(--divider);
  }
  .back-portrait {
    position: absolute;
    left: 60px;
    top: 190px;
    width: 430px;
    height: 354px;
  }
  /* Front cover */
  .front-cover {
    left: 608px;
    background: radial-gradient(ellipse at 50% 50%, var(--slate-light) 0%, var(--slate-dark) 100%);
  }
  .artist-name {
    position: absolute;
    top: 24px;
    left: 0;
    right: 0;
    margin: 0;
    text-align: center;
    font-family: "Crimson Text", Georgia, serif;
    font-weight: 600;
    font-size: 42px;
    letter-spacing: 0.3px;
    color: var(--ink-white);
  }
  .gilt-frame {
    position: absolute;
    left: 125px;
    top: 89px;
    width: 292px;
    height: 366px;
    filter: drop-shadow(0 3px 4px rgba(0,0,0,0.5));
  }
  .album-title {
    position: absolute;
    top: 468px;
    left: 0;
    right: 0;
    margin: 0;
    text-align: center;
    color: var(--ink-white);
  }
  .album-title-main {
    display: block;
    font-family: "Crimson Text", Georgia, serif;
    font-size: 19px;
    letter-spacing: 1px;
    line-height: 24px;
  }
  .album-title-number {
    font-family: "Alfa Slab One", Georgia, serif;
    font-size: 16px;
    letter-spacing: 1.5px;
  }
  .album-title-sub {
    display: block;
    font-family: "Alfa Slab One", Georgia, serif;
    font-size: 15px;
    letter-spacing: 1.4px;
    line-height: 22px;
  }
</style>
</head>
<body>
<main class="canvas">

  <section class="panel back-cover" aria-label="Back cover">
    <svg class="back-portrait" viewBox="0 0 430 354" role="img" aria-label="Painted portrait of the artist in a black t-shirt and gold chain, head bowed with hands on temples">
      <defs>
        <radialGradient id="backPortraitBody" cx="50%" cy="95%" r="62%">
          <stop offset="0%" stop-color="#1e1c1b"/>
          <stop offset="55%" stop-color="#2a2422"/>
          <stop offset="80%" stop-color="#3d3129" stop-opacity="0.55"/>
          <stop offset="100%" stop-color="#3d3129" stop-opacity="0"/>
        </radialGradient>
        <radialGradient id="backPortraitWarm" cx="50%" cy="42%" r="32%">
          <stop offset="0%" stop-color="#8a5a3e" stop-opacity="0.85"/>
          <stop offset="60%" stop-color="#5a3a2a" stop-opacity="0.45"/>
          <stop offset="100%" stop-color="#5a3a2a" stop-opacity="0"/>
        </radialGradient>
        <radialGradient id="backPortraitGold" cx="50%" cy="74%" r="14%">
          <stop offset="0%" stop-color="#d8c48a" stop-opacity="0.7"/>
          <stop offset="100%" stop-color="#d8c48a" stop-opacity="0"/>
        </radialGradient>
      </defs>
      <rect width="430" height="354" fill="url(#backPortraitBody)"/>
      <rect width="430" height="354" fill="url(#backPortraitWarm)"/>
      <rect width="430" height="354" fill="url(#backPortraitGold)"/>
    </svg>
    <ol class="tracklist tracklist-side-a">
      <li>1. Hollow Rooms</li>
      <li>2. Calm Ruler</li>
      <li>3. Fresh Mess</li>
      <li>4. Block Visions</li>
      <li>5. Brotha Workshop</li>
      <li>6. Anyone to Hold</li>
      <li>7. August Evenings</li>
      <li>8. Mae</li>
    </ol>
    <div class="tracklist-divider"></div>
    <ol class="tracklist tracklist-side-b">
      <li>Faith is my Anchor .9</li>
      <li>Tangles .10</li>
      <li>Proclaim .11</li>
      <li>Jubilee .12</li>
      <li>Our Thread .13</li>
      <li>Queen Chief .14</li>
      <li>318 .15</li>
      <li>Picture .16</li>
    </ol>
  </section>

  <section class="panel front-cover" aria-label="Front cover">
    <h1 class="artist-name">R.O.V.E.N.T.A. MARSH</h1>
    <svg class="gilt-frame" viewBox="0 0 292 366">
      <defs>
        <linearGradient id="giltSheen" x1="0" y1="0" x2="1" y2="1">
          <stop offset="0%" stop-color="var(--gold-pale)"/>
          <stop offset="18%" stop-color="var(--gold-mid)"/>
          <stop offset="34%" stop-color="var(--gold-light)"/>
          <stop offset="52%" stop-color="var(--gold-dark)"/>
          <stop offset="68%" stop-color="var(--gold-light)"/>
          <stop offset="84%" stop-color="var(--gold-mid)"/>
          <stop offset="100%" stop-color="var(--gold-deep)"/>
        </linearGradient>
        <radialGradient id="giltDepth" cx="50%" cy="50%" r="70%">
          <stop offset="60%" stop-color="#000" stop-opacity="0"/>
          <stop offset="100%" stop-color="#2a1a04" stop-opacity="0.45"/>
        </radialGradient>
        <linearGradient id="frontPortraitTone" x1="0" y1="0" x2="0" y2="1">
          <stop offset="0%" stop-color="#c4583a"/>
          <stop offset="22%" stop-color="#d98560"/>
          <stop offset="42%" stop-color="#b9b7bd"/>
          <stop offset="62%" stop-color="#9fa6b6"/>
          <stop offset="80%" stop-color="#6b5a52"/>
          <stop offset="100%" stop-color="#7a5547"/>
        </linearGradient>
        <radialGradient id="frontPortraitShade" cx="50%" cy="40%" r="70%">
          <stop offset="55%" stop-color="#2b1a14" stop-opacity="0"/>
          <stop offset="100%" stop-color="#2b1a14" stop-opacity="0.5"/>
        </radialGradient>
      </defs>
      <g role="img" aria-label="Ornate carved baroque gilt frame">
        <rect x="0" y="0" width="292" height="366" fill="url(#giltSheen)"/>
        <rect x="0" y="0" width="292" height="366" fill="url(#giltDepth)"/>
      </g>
      <rect x="2" y="2" width="288" height="362" fill="none" stroke="var(--gold-deep)" stroke-width="2"/>
      <rect x="28" y="26" width="236" height="314" fill="none" stroke="var(--gold-pale)" stroke-width="1.5"/>
      <rect x="34" y="32" width="224" height="302" fill="var(--gold-deep)"/>
      <rect x="38" y="35" width="216" height="296" fill="url(#frontPortraitTone)" role="img" aria-label="Oil-painted portrait of the artist in a white t-shirt and gold chain against a fiery red backdrop, dissolving like sand"/>
      <rect x="38" y="35" width="216" height="296" fill="url(#frontPortraitShade)"/>
    </svg>
    <p class="album-title">
      <span class="album-title-main">The <span class="album-title-number">318</span> Principle:</span>
      <span class="album-title-sub">Echoes of breathing</span>
    </p>
  </section>

</main>
</body>
</html>
```